依頼概要
ワークフェア関東2018の招待DMを
企業に対してお送りしたいと思っております。
A4サイズ表裏でデザイン頂きたく、
要素をpdfにまとめておりますのでご参考にお願いいたします。
イベント:ワークフェア http://www.workfair-sample.jp/
目的:フェアの弊社ブースまで誘致
商材:http://talentdesk-sample.jp/
送付先:採用ニーズがある関東圏の企業
同封物:フェア招待券3部と一緒に透明な袋に入れます
大事にすること:インパクト

面接革命ということでナポレオンを基調にデザインをお願いします。
今、表の下の部分は白背景に黒文字ですが全体をナポレオンにしていただいても
文字が埋もれないのであれば構いません。
https://files.example-share.jp/0703-b81d4e2a97c3f05d6e1a4b8c2f7d90e16

パワーポイントはこちらからダウンロードください

一番はっきりとわかりやすいデザインでした

みなさまご提案ありがとうございました。

```html
<!DOCTYPE html>
<html lang="ja">
<head>
<meta charset="utf-8">
<title>面接革命</title>
<link href="https://fonts.googleapis.com/css2?family=Dela+Gothic+One&family=Noto+Sans+JP:wght@500&display=swap" rel="stylesheet">
<style>
  :root {
    --red: #c8161e;
    --red-deep: #9e0c13;
    --white: #fbf7f4;
  }
  html, body {
    margin: 0;
    padding: 0;
    width: 857px;
    height: 1200px;
    overflow: hidden;
    background: var(--red);
  }
  .poster {
    position: relative;
    width: 857px;
    height: 1200px;
    overflow: hidden;
    background: var(--red);
  }
  .keyword-field {
    position: absolute;
    inset: 0;
    padding-top: 8px;
    font-family: "Noto Sans JP", sans-serif;
    font-weight: 500;
    font-size: 19px;
    letter-spacing: 0.55em;
    color: var(--red-deep);
    line-height: 37px;
    white-space: nowrap;
  }
  .keyword-row {
    display: block;
    margin-left: -10px;
  }
  .keyword-row.shift { margin-left: -70px; }
  .keyword-row.shift-2 { margin-left: 40px; }
  .headline {
    position: absolute;
    left: 0;
    top: 0;
    width: 857px;
    height: 1200px;
    margin: 0;
    font-family: "Dela Gothic One", sans-serif;
    font-weight: 400;
    color: var(--white);
    transform: rotate(-9deg);
    transform-origin: 430px 600px;
  }
  .headline-line {
    position: absolute;
    left: 0;
    width: 900px;
    font-size: 410px;
    line-height: 1;
    letter-spacing: -0.02em;
    white-space: nowrap;
    text-shadow: 0 0 1px var(--white);
  }
  .headline-line.top { top: 150px; left: 20px; }
  .headline-line.bottom { top: 560px; left: 40px; }
</style>
</head>
<body>
<main class="poster">
  <div class="keyword-field" aria-hidden="true">
    <span class="keyword-row">マッチング　面接ゼロ！　ミスマッチ　最適化！　マッチング</span>
    <span class="keyword-row shift">採用効率　４倍！　応募者管理　ゼロ！　面接　採用！</span>
    <span class="keyword-row shift-2">日程調整　手間なし！　自動データ化！　ストレスなし！</span>
    <span class="keyword-row">面接官の　スピード育成　進捗の見える化！　出会い！</span>
    <span class="keyword-row shift">評価シート　自動生成　求める人材との　出会い！</span>
    <span class="keyword-row shift-2">マッチング　面接ゼロ！　ミスマッチ　最適化！</span>
    <span class="keyword-row">採用効率　４倍！　応募者管理　ゼロ！　面接　採用！</span>
    <span class="keyword-row shift">日程調整　手間なし！　自動データ化！　ストレスなし！</span>
    <span class="keyword-row shift-2">面接官の　スピード育成　進捗の見える化！　出会い！</span>
    <span class="keyword-row">評価シート　自動生成　求める人材との　出会い！</span>
    <span class="keyword-row shift">マッチング　面接ゼロ！　ミスマッチ　最適化！</span>
    <span class="keyword-row shift-2">採用効率　４倍！　応募者管理　ゼロ！　面接　採用！</span>
    <span class="keyword-row">日程調整　手間なし！　自動データ化！　ストレスなし！</span>
    <span class="keyword-row shift">面接官の　スピード育成　進捗の見える化！　出会い！</span>
    <span class="keyword-row shift-2">評価シート　自動生成　求める人材との　出会い！</span>
    <span class="keyword-row">マッチング　面接ゼロ！　ミスマッチ　最適化！</span>
    <span class="keyword-row shift">採用効率　４倍！　応募者管理　ゼロ！　面接　採用！</span>
    <span class="keyword-row shift-2">日程調整　手間なし！　自動データ化！　ストレスなし！</span>
    <span class="keyword-row">面接官の　スピード育成　進捗の見える化！　出会い！</span>
    <span class="keyword-row shift">評価シート　自動生成　求める人材との　出会い！</span>
    <span class="keyword-row shift-2">マッチング　面接ゼロ！　ミスマッチ　最適化！</span>
    <span class="keyword-row">採用効率　４倍！　応募者管理　ゼロ！　面接　採用！</span>
    <span class="keyword-row shift">日程調整　手間なし！　自動データ化！　ストレスなし！</span>
    <span class="keyword-row shift-2">面接官の　スピード育成　進捗の見える化！　出会い！</span>
    <span class="keyword-row">評価シート　自動生成　求める人材との　出会い！</span>
    <span class="keyword-row shift">マッチング　面接ゼロ！　ミスマッチ　最適化！</span>
    <span class="keyword-row shift-2">採用効率　４倍！　応募者管理　ゼロ！　面接　採用！</span>
    <span class="keyword-row">日程調整　手間なし！　自動データ化！　ストレスなし！</span>
    <span class="keyword-row shift">面接官の　スピード育成　進捗の見える化！　出会い！</span>
    <span class="keyword-row shift-2">評価シート　自動生成　求める人材との　出会い！</span>
    <span class="keyword-row">マッチング　面接ゼロ！　ミスマッチ　最適化！</span>
    <span class="keyword-row shift">採用効率　４倍！　応募者管理　ゼロ！　面接　採用！</span>
  </div>
  <h1 class="headline">
    <span class="headline-line top">面接</span>
    <span class="headline-line bottom">革命</span>
  </h1>
</main>
</body>
</html>
```